Business Card & Full Stationary design For Summit Quarry
Summit Quarry For Marble & Granite
Business Card & Full Stationary design For Summit Quarry  - Construction
Creative Brief
Professional
Eng. Karim Haddouri
C.E.O
14 Shari' Nakhil el Wadi, Rawdatein, Giza, 12487, Egypt
kbh@summitquarry.com.eg
www.summitquarry.com.eg
we need everything to be included in the design ( CD, CD Cover, Letterhead, Envelopes, portfolio cover, etc..)
q7rimo q7rimo
I would highly appreciate if you can provide your concepts showing all the required stationaries including the back side of the B.Card ( Letterhead, 2 size envelope, Portfolio cover, CD, CD cover, Backgrounds for smartphones and Computers .)
Vonto Vonto

```html
<!DOCTYPE html>
<html lang="en">
<head>
<meta charset="utf-8">
<title>Summit Quarry – Business Card</title>
<link rel="stylesheet" href="https://fonts.googleapis.com/css2?family=Open+Sans:wght@300;400;600&display=swap">
<style>
  :root{
    --page:#e9e7e3;
    --card:#ffffff;
    --stone:#c8b99e;
    --stone-dark:#a8977a;
    --ink:#3a3631;
    --ink-soft:#6b655d;
  }
  *{margin:0;padding:0;box-sizing:border-box}
  html,body{width:1200px;height:876px;overflow:hidden}
  body{background:var(--page);font-family:"Open Sans",Arial,sans-serif;position:relative}
  .card{position:absolute;width:520px;height:300px;background:var(--card);border-radius:18px;
        box-shadow:0 10px 30px rgba(0,0,0,.12);overflow:hidden}
  .card--front{left:100px;top:110px}
  .card--back{left:580px;top:466px}

  .wordmark{color:var(--stone);font-weight:300;font-size:40px;letter-spacing:1px;white-space:nowrap}
  .card--front .wordmark{position:absolute;left:0;right:0;top:112px;text-align:center}
  .front__web{position:absolute;left:0;right:0;bottom:34px;text-align:center;font-size:12px;color:var(--ink);letter-spacing:.5px}

  .back__band{position:absolute;left:0;top:0;width:28px;height:100%;background:var(--stone)}
  .back__stripe{position:absolute;left:0;top:0}
  .back__header{position:absolute;left:28px;top:0;width:190px;height:74px;background:var(--stone);opacity:.35}
  .holder{position:absolute;left:44px;top:22px}
  .holder__name{font-size:16px;font-weight:600;color:var(--ink)}
  .holder__role{font-size:10px;color:var(--ink-soft);margin-top:1px}
  .address{position:absolute;left:44px;top:104px;font-size:9px;line-height:15px;color:var(--ink-soft)}
  .contacts{position:absolute;left:44px;top:206px;list-style:none;font-size:9.5px;line-height:17px;color:var(--ink)}
  .dots{position:absolute;left:9px;top:210px;display:flex;flex-direction:column;gap:7px}
  .dots span{width:10px;height:10px;border-radius:50%;background:var(--card)}
  .card--back .wordmark{position:absolute;left:230px;top:120px;width:270px;text-align:center;font-size:34px}
</style>
</head>
<body>
  <section class="card card--front">
    <p class="wordmark">Summit Quarry</p>
    <p class="front__web">www.summitquarry.com.eg</p>
  </section>

  <section class="card card--back">
    <div class="back__band"></div>
    <div class="back__header"></div>
    <svg class="back__stripe" width="60" height="300" viewBox="0 0 60 300">
      <polygon points="28,150 40,150 28,180" fill="#a8977a"/>
    </svg>
    <div class="holder">
      <p class="holder__name">Karim Haddouri</p>
      <p class="holder__role">General Manager</p>
    </div>
    <p class="address">14 Shari' Nakhil el Wadi<br>Rawdatein, Giza 12487</p>
    <div class="dots"><span></span><span></span><span></span><span></span></div>
    <ul class="contacts">
      <li>012 555 0147</li>
      <li>012 555 0148</li>
      <li>kbh@summitquarry.com.eg</li>
      <li>www.summitquarry.com.eg</li>
    </ul>
    <p class="wordmark">Summit Quarry</p>
  </section>
</body>
</html>
```